Business Card Design Project

Hi Designers, this project is currently on hold until the Logo is completed:
Please submit to the Logo project here:
http://jobs.pixelmarket.example/job.aspx?id=371905

Once logo is completed, it will be attached to this project for you to create business cards with show logo, company name and address

Maren T K Ashdown

Corwin's Meadow Pine Flock Co.
Hazelmere
Upper Brackwell
North Devon EX21 4TN

Tel: 01809 351846
Mobile: 07912 463078
email: maren@meadow-pine-flock.example
Updates

Project Deadline Extended
Reason: Sorry everyone, we have had a sick ewe and I am now behind with this one and need to extend the deadline. Best wishes Maren

The designer who wins the logo brief will be asked to design the business card. Many thanks Maren

Project Deadline Extended
Reason: Sorry everyone, just a chaotic time of year with animals. Need to extend the deadline again..... as I just haven't had enough time to take a good look.... Thank you for your understanding. Maren

Project Deadline Extended
Reason: Sorry everyone It is our busiest time of year with animals and just no time to spend going through such great designs. I will have to extend the deadline again and hopefully have some news very soon. Wishing you all a very happy Christmas and a happy and healthy new year. Maren & Corwin

Target Market(s)

High end market
Boutique restaurants for meat (it's not commercial lamb it's a slow matured quality meat more like venison/beef) expensive - specialized market

High End shoot clothing / wool / sheepskin rugs
Quality products

Industry/Entity Type

Business

Requirements
Must have
• based on the logo - (which Pixel Market has just been asked to do)
possibly based on a simplified picture of a Hebridean Ram (shows it's a Hebridean by it's horns as opposed to other black sheep!!)

```html
<!DOCTYPE html>
<html lang="en">
<head>
<meta charset="utf-8">
<title>Corwin's Meadow Pine Flock Co. — Business Cards</title>
<link rel="stylesheet" href="https://fonts.googleapis.com/css2?family=Questrial&display=swap">
<style>
  :root {
    --backdrop: #ececec;
    --card-dark: #26292a;
    --card-light: #ffffff;
    --ink-light: #f2f2f2;
    --ink-dark: #1d1d1d;
    --ink-muted: #6d6d6d;
    --shadow: rgba(0, 0, 0, 0.16);
  }
  * { box-sizing: border-box; margin: 0; padding: 0; }
  html, body {
    width: 1200px; height: 675px; overflow: hidden;
    background: var(--backdrop);
    font-family: "Questrial", "Century Gothic", sans-serif;
  }
  .stage {
    position: relative; width: 1200px; height: 675px;
    display: flex; align-items: center; justify-content: center; gap: 60px;
  }
  .card {
    position: relative; width: 510px; height: 292px;
    box-shadow: 0 6px 18px var(--shadow);
    overflow: hidden;
  }
  /* Front */
  .card--front { background: var(--card-dark); color: var(--ink-light); }
  .card__texture {
    position: absolute; inset: 0;
    background: linear-gradient(160deg, #2c2f30 0%, #232627 100%);
  }
  .front__content {
    position: absolute; inset: 0;
    display: flex; flex-direction: column; align-items: center; justify-content: center;
  }
  .brand-mark {
    width: 92px; height: 92px; border-radius: 50%;
    border: 5px solid var(--ink-light);
    margin-bottom: 14px;
  }
  .brand-name {
    font-size: 18px; letter-spacing: 2.5px; text-transform: uppercase;
    text-align: center; line-height: 1.35;
  }
  .front__url { margin-top: 22px; font-size: 15px; letter-spacing: 0.4px; }

  /* Back */
  .card--back { background: var(--card-light); color: var(--ink-dark); }
  .contact {
    position: absolute; left: 250px; top: 34px;
    font-size: 13px; line-height: 1.32;
  }
  .contact__company { font-weight: 400; }
  .contact__lines { margin-top: 10px; list-style: none; }
  .contact__lines li { display: flex; align-items: center; gap: 6px; }
  .contact__lines svg { width: 11px; height: 11px; flex: none; }
  .holder {
    position: absolute; left: 250px; top: 170px;
    font-size: 13px; letter-spacing: 0.6px; text-transform: uppercase;
  }
  .back__brand {
    position: absolute; left: 30px; bottom: 34px;
    display: flex; align-items: center; gap: 12px;
  }
  .back__brand .brand-mark {
    width: 50px; height: 50px; border: 3px solid var(--ink-dark); margin: 0;
  }
  .back__brand .brand-name {
    font-size: 13px; letter-spacing: 1.6px; text-align: left; color: var(--ink-dark);
  }
</style>
</head>
<body>
<main class="stage">
  <section class="card card--front">
    <div class="card__texture" role="img" aria-label="Faint repeating brand-mark pattern on charcoal"></div>
    <div class="front__content">
      <div class="brand-mark"></div>
      <p class="brand-name">Corwin's<br>Meadow Pine Flock Co.</p>
      <p class="front__url">www.meadow-pine-flock.example</p>
    </div>
  </section>

  <section class="card card--back">
    <address class="contact" style="font-style: normal;">
      <p class="contact__company">Corwin's Meadow Pine Flock Co.</p>
      <p>Hazelmere</p>
      <p>Upper Brackwell</p>
      <p>North Devon EX21 4TN</p>
      <ul class="contact__lines">
        <li>
          <svg viewBox="0 0 12 12" aria-label="Telephone"><rect width="12" height="12" rx="1.5" fill="#1d1d1d"/><path d="M3.5 2.8c.4-.3.9-.2 1.1.2l.6 1.1c.2.4 0 .7-.3.9l-.4.3c.4.9 1.1 1.6 2 2l.3-.4c.2-.3.6-.4.9-.2l1.1.6c.4.2.5.7.2 1.1-.5.7-1.3.9-2 .6C5 8.2 3.8 7 3 5 2.7 4.2 2.9 3.4 3.5 2.8z" fill="#fff"/></svg>
          01809 351846
        </li>
        <li>
          <svg viewBox="0 0 12 12" aria-label="Mobile"><rect x="2.5" y="0.5" width="7" height="11" rx="1" fill="none" stroke="#1d1d1d"/><rect x="3.8" y="2" width="4.4" height="6.5" fill="#1d1d1d"/></svg>
          07912 463078
        </li>
        <li>
          <svg viewBox="0 0 12 12" aria-label="Email"><rect x="0.5" y="2.5" width="11" height="7" fill="#1d1d1d"/><path d="M0.8 2.8L6 6.8l5.2-4" fill="none" stroke="#fff" stroke-width="0.9"/></svg>
          maren@meadow-pine-flock.example
        </li>
      </ul>
    </address>
    <p class="holder">Maren T K Ashdown</p>
    <div class="back__brand">
      <div class="brand-mark"></div>
      <p class="brand-name">Corwin's<br>Meadow Pine Flock Co.</p>
    </div>
  </section>
</main>
</body>
</html>
```